Need a new logo/business card for a cafe

I need a new logo and business card for a café. The café is called "Ladle", and we have a reputation for making a high quality cup of espresso coffee. I would like the business card design to reflect this "high quality". Our baristas craft our customers coffee with care to achieve this result. I would like to see designs that include a warm latte brown color. The card will be single sided to allow the rear to be used as a loyalty card which means the design will need to include space for our business address, phone number, and facebook page details. The uploaded logo is already in use on the café front window, and if it can be incorporated or used that would be great, but I am open to completely new designs as well. Thank you.
Updates
Thank you to all for the submissions. There's quite a few I like now, the hardest part will be choosing! I've set up a poll for added feedback from my own contacts and will wait on results from that.
Hello, more great designs coming in, thank you very much. There's quite a few that I really like, so my biggest challenge is going to be choosing one. Thanks again for your time, and I'll get onto the hard task of making that choice. Marcia
Industry/Entity Type
Cafe
Look and feel
Each slider illustrates characteristics of the customer's brand and the style your logo design should communicate.

```html
<!DOCTYPE html>
<html lang="en">
<head>
<meta charset="utf-8">
<title>Ladle – Business Card</title>
<link rel="stylesheet" href="https://fonts.googleapis.com/css2?family=Arvo&display=swap">
<style>
  :root {
    --backdrop: #1f1d1c;
    --latte: #9c8a7b;
    --latte-mid: #8a7a6d;
    --latte-deep: #76695e;
    --cream-strip: #b3a395;
    --roast: #4a3e37;
    --espresso: #14100e;
    --foam: #ffffff;
  }
  html, body {
    margin: 0;
    padding: 0;
    width: 1200px;
    height: 686px;
    overflow: hidden;
    background: var(--backdrop);
  }
  .canvas {
    position: relative;
    width: 1200px;
    height: 686px;
  }
  .card {
    position: absolute;
    left: 100px;
    top: 35px;
    width: 1000px;
    height: 616px;
    border-radius: 52px;
    overflow: hidden;
    background: var(--latte);
  }
  .card-bands {
    position: absolute;
    inset: 0;
    width: 100%;
    height: 100%;
    display: block;
  }
  .brand-name {
    position: absolute;
    left: 0;
    right: 0;
    top: 110px;
    margin: 0;
    text-align: center;
    font-family: "Arvo", serif;
    font-weight: 400;
    font-size: 120px;
    line-height: 1;
    color: var(--foam);
  }
  .contact-details {
    position: absolute;
    left: 0;
    right: 0;
    top: 458px;
    margin: 0;
    text-align: center;
    font-family: "Arvo", serif;
    font-size: 34px;
    line-height: 44px;
    color: var(--foam);
    font-style: normal;
  }
</style>
</head>
<body>
<main class="canvas">
  <section class="card">
    <svg class="card-bands" viewBox="0 0 792 488" preserveAspectRatio="none" aria-hidden="true">
      <path d="M0 290 Q396 302 792 296 L792 340 L0 340 Z" fill="var(--latte-mid)"/>
      <path d="M0 306 Q396 316 792 310 L792 340 L0 340 Z" fill="var(--latte-deep)"/>
      <rect x="0" y="324" width="792" height="9" fill="var(--cream-strip)"/>
      <rect x="0" y="333" width="792" height="155" fill="var(--roast)"/>
      <path d="M0 360 Q396 312 792 360 L792 488 L0 488 Z" fill="var(--espresso)"/>
    </svg>
    <h1 class="brand-name">Ladle</h1>
    <address class="contact-details">
      business address<br>
      phone number<br>
      and facebook
    </address>
  </section>
</main>
</body>
</html>
```